ISP 2 Page Magazine insert design

2 Page magazine insert design for advert in a digital and printed magazine for internet service provider.

All copy and brochure examples are provided in attached documents.

We require someone with infographic and similar design skills to put together a design that feels organic and part of the broader design as attached. Other competitors will be included, so we need to stand out.

There are specific guidelines by the magazine/brochure owner provided:

Leave 12,7mm x12,7mm space all around from the edge of the page till where the content should starts. Exceptions would be either an image that if purposefully meant to bleed off the page or a colour. (we would prefer a colour to bleed off the page)
Your header should be no lower than 43 mm from the top edge of the page.
If for any reason you decide to use Lorinet’s pink please note that it would be only accepted if it is the correct pink : C:0 M:100 Y:0 K:0 (100% Magenta). (We are OK with this, and would like the header to transition from their pink into our colours www.pebblarnet.co.za)
Page numbers will be included within the above mentioned 12,7 mm at the bottom of the page. (bottom of the page should be white
If need be; our text content font is within the Helvetica Neue family.
This is applicable to those who use a header and content to follow, please leave a 10mm gap between the header and the start of the body content.

Target Market(s)

Internet users

Industry/Entity Type

Internet Service Provider

Font styles to use
Other font styles liked:
• Helvetica Neue

Requirements
Must have
• Leave 12,7mm x12,7mm space all around from the edge of the page till where the content should starts. Exceptions would be either an image that if purposefully meant to bleed off the page or a colour. (we would prefer a colour to bleed off the page)
• Your header should be no lower than 43 mm from the top edge of the page.
• If for any reason you decide to use Lorinet’s pink please note that it would be only accepted if it is the correct pink : C:0 M:100 Y:0 K:0 (100% Magenta). (We are OK with this, and would like the header to transition from their pink into our colours www.pebblarnet.co.za)
• Page numbers will be included within the above mentioned 12,7 mm at the bottom of the page. (bottom of the page should be white
• If need be; our text content font is within the Helvetica Neue family.
• This is applicable to those who use a header and content to follow, please leave a 10mm gap between the header and the start of the body content.
Nice to have
• Bright colour integrated with the pink provided and our logo colours.

```html
<!DOCTYPE html>
<html lang="en">
<head>
<meta charset="utf-8">
<title>Pebblarnet – Make the Best Connection</title>
<link href="https://fonts.googleapis.com/css2?family=Archivo:ital,wdth,wght@1,125,900&family=Arimo:wght@400;700&display=swap" rel="stylesheet">
<style>
  :root {
    --brand-blue: #2f4ea5;
    --brand-lime: #9ef11a;
    --paper-light: #f4f4f5;
    --ink: #2a2a2a;
    --photo-light: #f2f3f4;
    --photo-mid: #c9ccd0;
  }
  * { margin: 0; padding: 0; box-sizing: border-box; }
  html, body { width: 900px; height: 1200px; overflow: hidden; background: var(--paper-light); }
  .insert {
    position: relative;
    width: 900px;
    height: 1200px;
    overflow: hidden;
    font-family: "Arimo", "Helvetica Neue", Arial, sans-serif;
    color: var(--ink);
  }
  .insert__shapes { position: absolute; inset: 0; }
  .headline-text {
    font-family: "Archivo", "Arial Black", sans-serif;
    font-style: italic;
    font-weight: 900;
    font-stretch: 125%;
    fill: var(--brand-blue);
  }
  .column { position: absolute; top: 794px; white-space: nowrap; }
  .column--about { left: 68px; width: 380px; }
  .column--products { left: 524px; width: 350px; }
  .column__title {
    font-weight: 700;
    font-size: 32px;
    line-height: 38px;
    color: var(--brand-blue);
    margin-bottom: 12px;
  }
  .column__body { font-size: 21px; line-height: 28px; color: var(--ink); }
  .column-divider {
    position: absolute;
    left: 467px; top: 804px;
    width: 3px; height: 212px;
    background: linear-gradient(to right, #b9b9bd, rgba(185,185,189,0));
  }
  .contact-list {
    position: absolute;
    left: 74px; top: 1072px;
    list-style: none;
    font-size: 21px;
    line-height: 28px;
    color: #1b1b1b;
  }
  .contact-list li { display: flex; align-items: center; gap: 11px; }
  .contact-list svg { width: 16px; height: 16px; flex: none; }
  .brand-name {
    position: absolute;
    left: 520px; top: 1046px;
    display: flex; align-items: center; gap: 12px;
  }
  .brand-name__dot { width: 24px; height: 24px; border-radius: 50%; background: var(--brand-lime); }
  .brand-name__text {
    font-weight: 700;
    font-size: 54px;
    line-height: 60px;
    color: var(--brand-blue);
    letter-spacing: -0.5px;
  }
</style>
</head>
<body>
<main class="insert">
  <svg class="insert__shapes" width="900" height="1200" viewBox="0 0 900 1200">
    <defs>
      <linearGradient id="paper" x1="0" y1="0" x2="0" y2="1">
        <stop offset="0" stop-color="#e2e2e5"/>
        <stop offset="0.5" stop-color="#f3f3f4"/>
        <stop offset="1" stop-color="#e6e6e8"/>
      </linearGradient>
      <linearGradient id="photo-tone" x1="0" y1="0" x2="1" y2="1">
        <stop offset="0" stop-color="#f2f3f4"/>
        <stop offset="0.55" stop-color="#dfe1e4"/>
        <stop offset="1" stop-color="#c9ccd0"/>
      </linearGradient>
    </defs>

    <rect class="paper" width="900" height="1200" fill="url(#paper)"/>
    <polygon class="paper-highlight" points="430,0 900,0 900,390 120,390" fill="#ececee"/>

    <text class="headline-text" x="46" y="120" font-size="82" textLength="806" lengthAdjust="spacingAndGlyphs">MAKE THE BEST</text>
    <text class="headline-text" x="46" y="190" font-size="82" textLength="774" lengthAdjust="spacingAndGlyphs">CONNECTION</text>

    <polygon class="hero-frame__lime" points="0,471 236,224 900,224 900,753 236,753" fill="var(--brand-lime)"/>
    <polygon class="hero-frame__blue" points="7,471 238,230 900,230 900,747 238,747" fill="var(--brand-blue)"/>
    <polygon class="hero-photo" role="img" aria-label="Photo of three smiling colleagues gathered around a laptop in a bright office"
             points="39,471 262,256 900,256 900,731 262,731" fill="url(#photo-tone)"/>

    <polygon class="footer-band__lime" points="0,1047 463,1047 608,1200 0,1200" fill="var(--brand-lime)"/>
    <polygon class="footer-band__blue" points="569,1154 900,1154 900,1200 612,1200" fill="var(--brand-blue)"/>
  </svg>

  <section class="column column--about">
    <h2 class="column__title">ABOUT US</h2>
    <p class="column__body">Built with the most modern fibre<br>optic broadband technology, and<br>delivered to you through infrastruc-<br>ture that stretches across the<br>country, the Pebblarnet network<br>is uncompromising in its quality.</p>
  </section>

  <div class="column-divider"></div>

  <section class="column column--products">
    <h2 class="column__title">FLEXIBLE<br>PRODUCTS</h2>
    <p class="column__body">For businesses and consum-<br>ers. We believe in making<br>things easy for you, so we take<br>the complexities out of<br>networking.</p>
  </section>

  <ul class="contact-list">
    <li>
      <svg viewBox="0 0 16 16"><circle cx="8" cy="8" r="6.8" fill="none" stroke="#2f4ea5" stroke-width="1.4"/><ellipse cx="8" cy="8" rx="3" ry="6.8" fill="none" stroke="#2f4ea5" stroke-width="1.2"/><line x1="1.2" y1="8" x2="14.8" y2="8" stroke="#2f4ea5" stroke-width="1.2"/></svg>
      NFO@PEBBLARNET.CO.ZA
    </li>
    <li>
      <svg viewBox="0 0 16 16"><rect x="1" y="1" width="14" height="14" rx="2" fill="#2f4ea5"/><path d="M5 4l2 1.5-1 1.5q1 2 3 3l1.5-1L12 11l-1.5 1.5Q6 11 3.5 5.5Z" fill="#fff"/></svg>
      27 21 555 0142
    </li>
    <li>
      <svg viewBox="0 0 16 16"><rect x="1" y="1" width="14" height="14" rx="2" fill="#2f4ea5"/><path d="M5 4l2 1.5-1 1.5q1 2 3 3l1.5-1L12 11l-1.5 1.5Q6 11 3.5 5.5Z" fill="#fff"/></svg>
      27 87 555 0187
    </li>
  </ul>

  <div class="brand-name">
    <span class="brand-name__dot"></span>
    <span class="brand-name__text">pebblarnet</span>
  </div>
</main>
</body>
</html>
```